Business Card Design

I need a business card design for my law office based in Pasadena, California. I am a sole practitioner and I specialize in business transaction and litigation, probate and estate planning, taxation law, corporate and business formation, immigration and real estate. I want something that is simple, yet stands out.

A friend helped to create a logo about 6 years ago. I am open to new ideas to changing the logo.

Industry/Entity Type

Business

Contact Information for Business Card

Law Offices of Dorvan L. Mabry
842 W. Larkspur Ave., Suite 319
Pasadena, CA 90287
Tel: 626-555-0174
Fax: 626-555-0139
Email: dmabry@dlmlegalgroup.example

Attorney: Dorvan L. Mabry

```html
<!DOCTYPE html>
<html lang="en">
<head>
<meta charset="utf-8">
<title>Dorvan L. Mabry — Business Cards</title>
<link rel="stylesheet" href="https://fonts.googleapis.com/css2?family=Cinzel:wght@400&family=Arimo:wght@400;700&display=swap">
<style>
  :root {
    --bg: #e9e6e1;
    --card: #ffffff;
    --ink: #1f1e1f;
    --band: #252324;
    --rule: #8a8a8a;
    --muted: #8c8c8c;
    --light: #f2f2f2;
  }
  * { margin: 0; padding: 0; box-sizing: border-box; }
  html, body { width: 1200px; height: 950px; overflow: hidden; }
  body {
    background: var(--bg);
    font-family: "Arimo", Arial, sans-serif;
    position: relative;
  }
  .card {
    position: absolute;
    width: 560px;
    height: 320px;
    background: var(--card);
    box-shadow: 0 6px 18px rgba(0,0,0,0.18);
    overflow: hidden;
  }
  .card--front { left: 70px; top: 80px; }
  .card--back { left: 570px; top: 540px; }

  .brand {
    position: absolute;
    display: flex;
    flex-direction: column;
    align-items: center;
    color: var(--ink);
    font-family: "Cinzel", Georgia, serif;
    font-weight: 400;
  }
  .brand__mark {
    width: 34px; height: 34px;
    background: var(--ink);
    margin-bottom: 14px;
  }
  .brand__name {
    font-size: 20px;
    letter-spacing: 1px;
    text-align: center;
    line-height: 1.5;
    padding-top: 6px;
    border-top: 1px solid var(--rule);
  }
  .brand__name span { display: block; font-size: 11px; letter-spacing: 3px; }

  .card--front .brand { left: 0; right: 0; top: 82px; }
  .website {
    position: absolute;
    left: 0; right: 0; top: 232px;
    text-align: center;
    font-size: 13px;
    letter-spacing: 2px;
    color: #555;
  }

  .band { position: absolute; inset: 0; }
  .contact {
    position: absolute;
    left: 28px; top: 62px;
    color: var(--light);
    font-size: 14px;
    line-height: 21px;
    list-style: none;
  }
  .contact li { display: flex; align-items: center; gap: 9px; }
  .contact svg { width: 13px; height: 13px; flex: none; }
  .contact .address { padding-left: 0; margin-top: 4px; display: block; }

  .card--back .brand { left: 330px; top: 100px; width: 210px; }
  .card--back .brand__name { font-size: 18px; }

  .person { position: absolute; left: 28px; top: 246px; }
  .person__name { font-size: 19px; font-weight: 700; color: var(--ink); }
  .person__title { font-size: 13px; color: var(--muted); margin-top: 3px; }
</style>
</head>
<body>

<section class="card card--front">
  <div class="brand">
    <div class="brand__mark"></div>
    <div class="brand__name"><span>Law Offices of</span>Dorvan L. Mabry</div>
  </div>
  <p class="website">www.dlmlegalgroup.example</p>
</section>

<section class="card card--back">
  <svg class="band" viewBox="0 0 560 320" aria-hidden="true">
    <polygon points="0,0 380,0 262,180 0,196" fill="var(--band)"/>
    <polyline points="392,0 272,186 0,204" fill="none" stroke="var(--rule)" stroke-width="2"/>
  </svg>

  <ul class="contact">
    <li>
      <svg viewBox="0 0 16 16"><path fill="currentColor" d="M3 1h3l1 4-2 1c1 2 3 4 5 5l1-2 4 1v3c0 1-1 2-2 2C7 15 1 9 1 3c0-1 1-2 2-2z"/></svg>
      626-555-0174
    </li>
    <li>
      <svg viewBox="0 0 16 16"><path fill="currentColor" d="M4 1h8v4H4zM1 6h14v7h-3v2H4v-2H1zM5 10v4h6v-4z"/></svg>
      626-555-0139
    </li>
    <li>
      <svg viewBox="0 0 16 16"><path fill="currentColor" d="M1 3h14v10H1zM2 4.5v.5l6 4 6-4v-.5z"/></svg>
      dmabry@dlmlegalgroup.example
    </li>
    <li class="address">842 W. Larkspur Ave.<br>Suite 319<br>Pasadena, CA 90287</li>
  </ul>

  <div class="brand">
    <div class="brand__mark"></div>
    <div class="brand__name"><span>Law Offices of</span>Dorvan L. Mabry</div>
  </div>

  <div class="person">
    <p class="person__name">Dorvan L. Mabry</p>
    <p class="person__title">CEO/Founder</p>
  </div>
</section>

</body>
</html>
```